Tavlune

I'd like new business card design options. I'll need to provide updated contact info although after the deign is complete. We are in IT, specifically in the data backup, archiving and disaster recovery verticals.

Business

```html
<!DOCTYPE html>
<html lang="en">
<head>
<meta charset="utf-8">
<title>Tavlune Business Cards</title>
<link rel="stylesheet" href="https://fonts.googleapis.com/css2?family=Montserrat:wght@400;500;600;700&family=Oswald:wght@500&display=swap">
<style>
  :root {
    --bg: #8d9194;
    --card-back: #aac8e4;
    --card-front: #ffffff;
    --brand-blue: #1e5fae;
    --band-blue: #2a6cc2;
    --name-blue: #3d86d4;
    --text-grey: #5c6670;
    --strip-light: #eef3f8;
    --navy: #233e6a;
    --white: #ffffff;
  }
  * { box-sizing: border-box; margin: 0; padding: 0; }
  html, body { width: 1200px; height: 862px; overflow: hidden; }
  body {
    background: var(--bg);
    font-family: "Montserrat", Arial, sans-serif;
    position: relative;
  }
  .card {
    position: absolute;
    width: 520px;
    height: 297px;
    border-radius: 4px;
    overflow: hidden;
    box-shadow: 0 10px 24px rgba(0,0,0,0.25);
  }
  .card--back { left: 50px; top: 282px; background: var(--card-back); }
  .card--front { left: 630px; top: 282px; background: var(--card-front); }

  .wordmark { position: absolute; display: flex; align-items: center; gap: 10px; }
  .wordmark__dot { width: 30px; height: 30px; border-radius: 50%; background: var(--brand-blue); }
  .wordmark__name {
    font-weight: 700; font-size: 26px; letter-spacing: 0.5px; color: var(--brand-blue);
    line-height: 1;
  }
  .wordmark__tagline {
    font-size: 10px; font-weight: 500; letter-spacing: 0.3px; color: var(--brand-blue); margin-top: 4px;
  }

  .contact { position: absolute; font-size: 11.5px; color: var(--text-grey); line-height: 1.35; }
  .contact__name { font-size: 14px; font-weight: 500; color: var(--name-blue); }
  .contact__title { font-size: 9px; letter-spacing: 0.5px; text-transform: uppercase; }
  .contact__gap { height: 10px; }
  .contact__web { font-weight: 700; color: var(--brand-blue); font-size: 12.5px; }

  .services {
    position: absolute; left: 0; right: 0; bottom: 0; height: 40px;
    display: flex; align-items: center; justify-content: center; gap: 12px;
    font-family: "Oswald", "Arial Narrow", sans-serif; font-weight: 500;
    font-size: 13px; letter-spacing: 1.6px; text-transform: uppercase;
  }
  .services__sep { opacity: 0.7; }

  /* back card */
  .card--back .wordmark { left: 40px; top: 110px; }
  .divider { position: absolute; left: 250px; top: 60px; width: 1px; height: 150px; background: rgba(255,255,255,0.75); }
  .card--back .contact { left: 270px; top: 40px; color: var(--white); }
  .card--back .contact__name { color: var(--brand-blue); }
  .card--back .contact__web { color: var(--navy); }
  .card--back .services { background: var(--strip-light); color: var(--navy); }

  /* front card */
  .network-art {
    position: absolute; left: 150px; top: 0; width: 370px; height: 257px;
    background: radial-gradient(ellipse at 45% 55%, #d2dbe4 0%, #e8eef3 45%, #ffffff 85%);
  }
  .card--front .wordmark { left: 32px; top: 94px; }
  .card--front .contact { left: 300px; top: 30px; }
  .address {
    position: absolute; left: 132px; top: 182px;
    font-size: 13px; color: var(--text-grey); line-height: 1.35;
  }
  .card--front .services { background: var(--band-blue); color: var(--white); }
</style>
</head>
<body>

<section class="card card--back" aria-label="Business card, back">
  <div class="wordmark">
    <span class="wordmark__dot"></span>
    <div>
      <div class="wordmark__name">Tavlune</div>
      <div class="wordmark__tagline">Backup You Can Trust</div>
    </div>
  </div>
  <div class="divider"></div>
  <div class="contact">
    <div class="contact__name">Marcus L. Whitfield, Ph. D</div>
    <div class="contact__title">President, CTO</div>
    <div>marcus.whitfield@tavlune.com</div>
    <div class="contact__gap"></div>
    <div>4418 Meridian Ave.</div>
    <div>PO Box 620947</div>
    <div>Lakemont, TX 75231-0947</div>
    <div class="contact__gap"></div>
    <div>Phone: 800-555-0142</div>
    <div>Fax: 888-555-0187</div>
    <div class="contact__gap"></div>
    <div class="contact__web">www.tavlune.com</div>
  </div>
  <div class="services">
    <span>Online PC Backup</span><span class="services__sep">|</span>
    <span>Continuous Server Backup</span><span class="services__sep">|</span>
    <span>Data Archiving</span>
  </div>
</section>

<section class="card card--front" aria-label="Business card, front">
  <div class="network-art" role="img" aria-label="Faint connected network nodes and lines in soft grey"></div>
  <div class="wordmark">
    <span class="wordmark__dot"></span>
    <div>
      <div class="wordmark__name">Tavlune</div>
      <div class="wordmark__tagline">Backup You Can Trust</div>
    </div>
  </div>
  <div class="contact">
    <div class="contact__name">Marcus L. Whitfield, Ph. D</div>
    <div class="contact__title">President, CTO</div>
    <div>marcus.whitfield@tavlune.com</div>
    <div class="contact__gap"></div>
    <div>Phone: 800-555-0142</div>
    <div>Fax: 888-555-0187</div>
    <div class="contact__web">www.tavlune.com</div>
  </div>
  <div class="address">
    <div>4418 Meridian Ave.</div>
    <div>PO Box 620947</div>
    <div>Lakemont, TX 75231-0947</div>
  </div>
  <div class="services">
    <span>Online PC Backup</span><span class="services__sep">|</span>
    <span>Continuous Server Backup</span><span class="services__sep">|</span>
    <span>Data Archiving</span>
  </div>
</section>

</body>
</html>
```